Professional Home Buyer business card needed

I need a pretty straight forward business card designed. We help people that NEED to sell their homes solve problems. We perform all types of Real Estate transactions including flip, wholesale, investment, rental property and multi family. The card will mainly be used to give to prospective Sellers but will also be given to Real Estate Investors as well. It should professional and very easy to read, most clients are older people.

Target Market(s)

Distressed home sellers as well as Real Estate investors

Industry/Entity Type

Real Estate

Contact Information for Business Card

should be a professional layout

Colors
ec1f27
ffffff
000000

Requirements
Must have
• Large logo on back and smaller one on front. should utilize Red, white, and black.
• I am thinking of using a soft touch coating on the card so keep that in mind.
• Contact info should be very easy to read, think older clients.
Nice to have
• I would like to see a design with rounded corners on the card
Should not have
• pictures of homes or other home graphics.

```html
<!DOCTYPE html>
<html lang="en">
<head>
<meta charset="utf-8">
<title>Keystone Home Buyers – Business Card</title>
<link href="https://fonts.googleapis.com/css2?family=Open+Sans:wght@400;600;700;800&display=swap" rel="stylesheet">
<style>
  :root {
    --red: #ec1f27;
    --white: #ffffff;
    --black: #000000;
    --stage: #2a2a2a;
  }
  html, body {
    margin: 0;
    padding: 0;
    overflow: hidden;
  }
  body {
    width: 1200px;
    height: 892px;
    background: var(--stage);
    position: relative;
    font-family: "Open Sans", Arial, sans-serif;
  }
  .card {
    position: absolute;
    width: 560px;
    height: 320px;
    overflow: hidden;
    box-shadow: 0 14px 30px rgba(0,0,0,0.55);
  }

  /* Back of card */
  .card-back {
    left: 40px;
    top: 110px;
    background: var(--red);
  }
  .back-brand {
    position: absolute;
    left: 0;
    right: 0;
    top: 118px;
    display: flex;
    justify-content: center;
    align-items: center;
    gap: 14px;
  }
  .brand-square {
    width: 22px;
    height: 22px;
    background: var(--white);
  }
  .back-brand .brand-name {
    color: var(--white);
    font-weight: 800;
    font-size: 52px;
    letter-spacing: 1px;
    line-height: 1;
  }
  .back-web {
    position: absolute;
    left: 0;
    right: 0;
    bottom: 44px;
    margin: 0;
    text-align: center;
    color: var(--white);
    font-size: 15px;
    letter-spacing: 3px;
  }

  /* Front of card */
  .card-front {
    left: 600px;
    top: 462px;
    background: var(--white);
  }
  .front-panel {
    position: absolute;
    inset: 0;
  }
  .contact-name {
    position: absolute;
    left: 40px;
    top: 96px;
    margin: 0;
    color: var(--red);
    font-weight: 700;
    font-size: 20px;
    line-height: 1.1;
  }
  .contact-title {
    position: absolute;
    left: 40px;
    top: 120px;
    margin: 0;
    color: var(--white);
    font-size: 14px;
  }
  .contact-address {
    position: absolute;
    left: 40px;
    top: 198px;
    margin: 0;
    color: var(--white);
    font-size: 14px;
    line-height: 1.3;
    font-style: normal;
  }
  .contact-list {
    position: absolute;
    left: 40px;
    top: 240px;
    margin: 0;
    padding: 0;
    list-style: none;
    color: var(--white);
    font-size: 14px;
    line-height: 1.4;
  }
  .contact-list li {
    display: flex;
    align-items: center;
    gap: 10px;
  }
  .contact-list svg {
    width: 13px;
    height: 13px;
    fill: var(--red);
    flex: none;
  }
  .front-brand {
    position: absolute;
    left: 310px;
    right: 18px;
    top: 110px;
    text-align: center;
  }
  .tagline {
    margin: 0 0 6px;
    font-size: 9px;
    font-weight: 600;
    letter-spacing: 2.5px;
    color: var(--black);
  }
  .front-brand .brand-name {
    margin: 0;
    font-weight: 800;
    font-size: 36px;
    line-height: 1;
    color: var(--black);
    letter-spacing: 1px;
  }
  .front-brand .brand-sub {
    margin: 6px 0 0;
    font-weight: 800;
    font-size: 16px;
    letter-spacing: 4px;
    color: var(--black);
  }
</style>
</head>
<body>

<section class="card card-back" aria-label="Card back">
  <div class="back-brand">
    <span class="brand-square"></span>
    <span class="brand-name">KEYSTONE</span>
  </div>
  <p class="back-web">www.keystonehomebuyer.com</p>
</section>

<section class="card card-front" aria-label="Card front">
  <svg class="front-panel" width="560" height="320" viewBox="0 0 560 320" aria-hidden="true">
    <polygon points="0,0 232,0 292,112 300,320 0,320" fill="var(--black)"/>
    <polyline points="232,0 292,112 300,320" fill="none" stroke="var(--red)" stroke-width="3"/>
  </svg>

  <h1 class="contact-name">MARA LINDQVIST</h1>
  <p class="contact-title">PRESIDENT</p>

  <address class="contact-address">2716 Alder Crest Lane<br>Maple Bend, NY 11090</address>

  <ul class="contact-list">
    <li>
      <svg viewBox="0 0 16 16"><path d="M3 1h3l1.5 4-2 1.3a9 9 0 0 0 4.2 4.2L11 8.5l4 1.5v3c0 1-1 2-2 2C6.5 15 1 9.5 1 3c0-1 1-2 2-2z"/></svg>
      <span>555 014 7680</span>
    </li>
    <li>
      <svg viewBox="0 0 16 16"><path d="M4 0h8a1 1 0 0 1 1 1v14a1 1 0 0 1-1 1H4a1 1 0 0 1-1-1V1a1 1 0 0 1 1-1zm1 2v10h6V2zm3 11a1 1 0 1 0 0 2 1 1 0 0 0 0-2z"/></svg>
      <span>555 019 3412</span>
    </li>
    <li>
      <svg viewBox="0 0 16 16"><path d="M0 3h16v1L8 9 0 4zm0 3 8 5 8-5v7H0z"/></svg>
      <span>mara@keystonehomebuyer.com</span>
    </li>
  </ul>

  <div class="front-brand">
    <p class="tagline">WE MAKE SELLING SIMPLE!</p>
    <p class="brand-name">KEYSTONE</p>
    <p class="brand-sub">HOME BUYERS</p>
  </div>
</section>

</body>
</html>
```